Business Name: MT Property Styling Pty Ltd

Business Type: Professional Home Styling and Minor Renovation Business

Logo: Attached is the logo that has been created.
I always envisaged the logo in the middle of the business card with my full name underneath it.

Maren Tulloch B.Com RVA DMH
Property Stylist & Project Manager

Include dot points of services
Staging Houses for Sale
Minor Home Renovations
Home Styling & Project Management
Re-Designing Living Spaces to Aid the Disabled

Somewhere on the card I would like to incorporate
"Property Styling and Cosmetic Renovations"

Colour Scheme:
Gloss black business card, with white and then
Gold or Silver as the highlight colours.

Incorporate a small amount of yellow only if possible to make it pop. If this really doesn’t work it doesn’t have to be used. Also l like the colour teal if that needs to be used as a contrast colour.

Feel/Themes
• I love antique chairs, regal expensive looking furniture mixed with modern homes (this is the unique style I want to sell) antique and modern mix that looks high class as well as modern and fresh, targeting an executive market.
• I want to use an orchid as a trademark throughout the course of my work, not sure if this can somehow be incorporated? Also really like crowns to give that regal/antique feel and then something else to give that modern twist (I don’t know what the something else could be)
• Wall Paper Look (on a portion of it not all of it, like a French look)
• Overall feel - A very deluxe and professional feel with a little bit of creative flare.

I hope this helps create a bit of a picture.

Is it ok that I call you tomorrow morning? My mobile number is 0491 862 574 if you have any questions for me in the meantime.

Target Market(s)

High Quality Executive Market - People selling homes

Industry/Entity Type

Business

Contact Information for Business Card

Include dot points of services:
Staging Houses for Sale
Minor Home Renovations

Font styles to use
Serif
Script

Colors
33b8a4
fbed22

Requirements
Must have
• Maren Tulloch B.Com RVA DMH
• Property Stylist & Project Manager
• RVA and DMH Logos on the card
• "Dramatically increase the value of your property"
Nice to have
• Colour Scheme:
• Gloss black business card, with white and then
• Gold or Silver as the highlight colours.
• Incorporate a small amount of yellow only if possible to make it pop. If this really doesn’t work it doesn’t have to be used. Also l like the colour teal if that needs to be used as a contrast colour.
• Also like teal as a highlight colour.

```html
<!DOCTYPE html>
<html lang="en">
<head>
<meta charset="utf-8">
<title>MT Property Styling Pty Ltd – Business Card</title>
<link href="https://fonts.googleapis.com/css2?family=Great+Vibes&family=Cormorant+Garamond:wght@500&family=Tinos&display=swap" rel="stylesheet">
<style>
  :root{
    --stage:#3b3b3d;
    --card:#ffffff;
    --ink:#1b1b1b;
    --black:#0d0d0d;
    --gold:#c9a445;
    --gold-light:#f1d98a;
    --gold-deep:#8f6a1f;
    --white:#ffffff;
  }
  *{margin:0;padding:0;box-sizing:border-box}
  html,body{width:1200px;height:852px;overflow:hidden;background:var(--stage)}
  .stage{position:relative;width:1200px;height:852px}
  .card{position:absolute;width:520px;height:300px;background:var(--card);border-radius:14px;overflow:hidden;box-shadow:0 10px 28px rgba(0,0,0,.45)}
  .card--services{left:70px;top:130px}
  .card--contact{left:610px;top:420px}
  .card svg.swoosh{position:absolute;left:0;top:0;width:520px;height:300px}

  .brand{position:absolute;display:flex;align-items:center;gap:9px;font-family:"Cormorant Garamond",serif;font-weight:500;color:var(--gold-deep);letter-spacing:.05em;text-transform:uppercase;white-space:nowrap}
  .brand__dot{width:11px;height:11px;border-radius:50%;background:var(--gold)}
  .card--services .brand{left:170px;top:52px;font-size:18px}
  .card--contact .brand{left:214px;top:44px;font-size:15px}

  .badge{position:absolute;background:var(--black)}
  .badge--dmh{left:250px;top:104px;width:84px;height:70px}
  .badge--rva{left:346px;top:82px;width:150px;height:92px;border:2px solid var(--black);background:var(--white)}
  .badge--rva span{position:absolute;left:0;top:0;width:100px;height:100%;background:#2a2522}

  .services{position:absolute;left:26px;top:178px;list-style:none;font-family:"Tinos",serif;font-size:13.5px;line-height:20px;color:var(--ink)}
  .services li::before{content:"» ";}

  .person{position:absolute;left:30px;top:62px}
  .person__name{font-family:"Great Vibes",cursive;font-weight:400;font-size:34px;color:var(--ink);line-height:1}
  .person__role{margin-top:10px;font-family:"Tinos",serif;font-size:14px;line-height:17px;color:var(--ink)}

  .contact{position:absolute;left:30px;top:196px;list-style:none;font-family:"Tinos",serif;font-size:14px;line-height:22px;color:var(--ink)}
  .contact li{display:flex;align-items:center;gap:10px}
  .contact svg{width:13px;height:13px;fill:var(--ink)}

  .tagline{position:absolute;right:18px;top:166px;width:140px;text-align:right;font-family:"Tinos",serif;font-size:14px;line-height:19px;color:var(--white)}
</style>
</head>
<body>
<main class="stage">

  <section class="card card--services" aria-label="Business card front: services">
    <svg class="swoosh" viewBox="0 0 520 300" aria-hidden="true">
      <defs>
        <linearGradient id="goldBand" x1="0" y1="1" x2="1" y2="0">
          <stop offset="0" stop-color="#8f6a1f"/>
          <stop offset=".5" stop-color="#f1d98a"/>
          <stop offset="1" stop-color="#c9a445"/>
        </linearGradient>
      </defs>
      <path d="M300,300 C390,280 460,262 520,248 L520,300 Z" fill="#0d0d0d"/>
      <path d="M240,300 C350,276 440,250 520,232" fill="none" stroke="url(#goldBand)" stroke-width="7"/>
    </svg>
    <div class="brand"><span class="brand__dot"></span>MT Property Styling Pty Ltd</div>
    <div class="badge badge--dmh" role="img" aria-label="DMH membership badge"></div>
    <div class="badge badge--rva" role="img" aria-label="RVA membership badge"><span></span></div>
    <ul class="services">
      <li>Staging Homes for Sale</li>
      <li>Minor Home Renovations</li>
      <li>Source Furnishings &amp; Accessories</li>
      <li>Re-Designing Rooms for the Disabled</li>
      <li>Home Styling, Project &amp; Budget Management</li>
    </ul>
  </section>

  <section class="card card--contact" aria-label="Business card back: contact">
    <svg class="swoosh" viewBox="0 0 520 300" aria-hidden="true">
      <defs>
        <linearGradient id="goldWave" x1="0" y1="1" x2="1" y2="0">
          <stop offset="0" stop-color="#8f6a1f"/>
          <stop offset=".45" stop-color="#f1d98a"/>
          <stop offset="1" stop-color="#c9a445"/>
        </linearGradient>
      </defs>
      <path d="M520,66 C430,72 380,124 350,182 C320,240 280,292 200,300 L520,300 Z" fill="#0d0d0d"/>
      <path d="M130,300 C250,292 300,244 330,190 C362,132 420,64 520,54" fill="none" stroke="url(#goldWave)" stroke-width="6"/>
      <path d="M160,286 C260,276 300,236 322,198" fill="none" stroke="url(#goldWave)" stroke-width="2"/>
      <path d="M110,300 C220,298 290,280 330,246" fill="none" stroke="url(#goldWave)" stroke-width="3"/>
    </svg>
    <div class="brand"><span class="brand__dot"></span>MT Property Styling Pty Ltd</div>
    <div class="person">
      <h1 class="person__name">Maren Tulloch</h1>
      <p class="person__role">B.Com RVA DMH<br>Property Stylist &amp;<br>Project Manager</p>
    </div>
    <ul class="contact">
      <li><svg viewBox="0 0 16 16" aria-hidden="true"><path d="M3 1l3 3-2 2c1 2 3 4 5 5l2-2 3 3-2 3C6 15 1 10 1 3z"/></svg>00 00 000 00 0</li>
      <li><svg viewBox="0 0 16 16" aria-hidden="true"><path d="M1 3h14v10H1z M2 4l6 5 6-5" fill="none" stroke="#1b1b1b" stroke-width="1.4"/><path d="M1 3h14v1.5L8 10 1 4.5z"/></svg>yourname@yourwebsite.com</li>
      <li><svg viewBox="0 0 16 16" aria-hidden="true"><circle cx="8" cy="8" r="7"/></svg>www.yourwebsite.com</li>
    </ul>
    <p class="tagline">Dramatically Increase the Value of Your Home</p>
  </section>

</main>
</body>
</html>
```